Geschäftspapiere für Rechtsberatung
Zielgruppe
Rechtsberatung; Zielgruppe sind sowohl Privat- als auch Geschäftsleute
Die Einzelkanzlei von Marlene Kosswig (Näheres siehe www.kosswig-beispiel.de) wird zu einer Partnergesellschaft, der
Kosswig

```html
<!DOCTYPE html>
<html lang="de">
<head>
<meta charset="utf-8">
<title>Briefbogen – Rechtsanwaltskanzlei Marlene Kosswig</title>
<link rel="stylesheet" href="https://fonts.googleapis.com/css2?family=Crimson+Pro:wght@400;600;700&family=Open+Sans:wght@400&display=swap">
<style>
  :root {
    --brand-red: #9b1b1f;
    --ink: #1e1e1e;
    --ink-soft: #555555;
    --paper: #ffffff;
    --backdrop: #eeeeee;
    --mark: #b5b5b5;
  }
  * { margin: 0; padding: 0; box-sizing: border-box; }
  html, body {
    width: 1200px; height: 861px; overflow: hidden;
    background: var(--backdrop);
  }
  .letterhead {
    position: absolute; left: 302px; top: 10px;
    width: 595px; height: 842px;
    background: var(--paper);
    font-family: "Crimson Pro", "Palatino Linotype", serif;
    color: var(--ink);
    box-shadow: 0 1px 3px rgba(0,0,0,.12);
  }
  .rule { position: absolute; height: 1.3px; background: var(--brand-red); }
  .rule--head-left { left: 57px; width: 198px; top: 45px; }
  .rule--head-right { left: 341px; width: 212px; top: 45px; }
  .rule--foot-left { left: 57px; width: 225px; top: 714px; }
  .rule--foot-right { left: 313px; width: 240px; top: 714px; }
  .brand-dot { position: absolute; border-radius: 50%; background: var(--brand-red); }
  .brand-dot--head { left: 268px; top: 17px; width: 58px; height: 58px; }
  .brand-dot--foot { left: 287px; top: 704px; width: 20px; height: 20px; }
  .firm-kicker {
    position: absolute; top: 86px; left: 0; width: 595px; text-align: center;
    font-family: "Open Sans", Arial, sans-serif; font-size: 9.5px; color: var(--ink);
  }
  .firm-name {
    position: absolute; top: 99px; left: 0; width: 595px; text-align: center;
    font-size: 16px; color: #333;
  }
  .sender-line {
    position: absolute; left: 57px; top: 156px; font-size: 7.5px; color: var(--ink);
  }
  .sender-line strong { color: var(--brand-red); font-weight: 700; }
  .ref-fields {
    position: absolute; left: 395px; top: 154px; font-size: 9px; line-height: 17px; color: var(--ink-soft);
  }
  .fold-mark { position: absolute; height: 1px; background: var(--mark); }
  .fold-mark--upper { left: 0; top: 299px; width: 8px; }
  .fold-mark--punch { left: 34px; top: 422px; width: 18px; }
  .fold-mark--lower { left: 0; top: 596px; width: 8px; }
  .footer-col {
    position: absolute; top: 740px; font-size: 10.5px; line-height: 14px; color: var(--ink-soft);
  }
  .footer-col--identity { left: 57px; }
  .footer-col--identity .footer-firm { color: var(--ink); font-weight: 700; margin-bottom: 6px; }
  .footer-col--contact { left: 256px; }
  .footer-col--bank { left: 411px; }
  .footer-row { display: flex; }
  .footer-label { width: 34px; }
  .footer-col--bank .footer-label { width: 54px; }
  .footer-gap { height: 6px; }
</style>
</head>
<body>
  <main class="letterhead">
    <div class="rule rule--head-left"></div>
    <div class="brand-dot brand-dot--head"></div>
    <div class="rule rule--head-right"></div>
    <p class="firm-kicker">Rechtsanwaltskanzlei</p>
    <p class="firm-name">Marlene Kosswig</p>

    <p class="sender-line"><strong>Kosswig § Brandtner PartG mbB</strong> • Lindenweg 12 • 45100 Musterstadt</p>
    <div class="ref-fields">
      <p>Datum:</p>
      <p>Unser Zeichen:</p>
    </div>

    <div class="fold-mark fold-mark--upper"></div>
    <div class="fold-mark fold-mark--punch"></div>
    <div class="fold-mark fold-mark--lower"></div>

    <div class="rule rule--foot-left"></div>
    <div class="brand-dot brand-dot--foot"></div>
    <div class="rule rule--foot-right"></div>

    <footer>
      <div class="footer-col footer-col--identity">
        <p class="footer-firm">Kosswig § Brandtner PartG mbB<br>Marlene Kosswig</p>
        <p>Dipl.-Juristin</p>
        <p>Lindenweg 12</p>
        <p>45100 Musterstadt</p>
      </div>
      <div class="footer-col footer-col--contact">
        <div class="footer-row"><span class="footer-label">Tel.:</span><span>02301/554700</span></div>
        <div class="footer-row"><span class="footer-label">Fax:</span><span>02301/5547002</span></div>
        <div class="footer-row"><span class="footer-label">Mobil:</span><span>0171/5547003</span></div>
        <div class="footer-gap"></div>
        <div class="footer-row"><span class="footer-label">Mail:</span><span>info@kosswig-beispiel.de</span></div>
        <div class="footer-row"><span class="footer-label">Web:</span><span>www.kosswig-beispiel.de</span></div>
      </div>
      <div class="footer-col footer-col--bank">
        <p>Musterbank</p>
        <div class="footer-row"><span class="footer-label">IBAN:</span><span>DE5012345678<br>0099887766</span></div>
        <div class="footer-row"><span class="footer-label">BIC:</span><span>MUSTDEX1001</span></div>
        <div class="footer-gap"></div>
        <div class="footer-row"><span class="footer-label">Steuer-Nr.</span><span>XXX XXX XXX XXX</span></div>
      </div>
    </footer>
  </main>
</body>
</html>
```